Bramwell Business Card Design

hello,
we are looking for a business card design for our Fintech Company. We are credit card processing company that is also expanding in to the crypto market. We will be focusing on crypto processing, with a crypto wallet and crypto exchange. We like the purple in the logo. We want something modern and sophisticated but at the same time simple and trust worthy to work with banks.

Industry/Entity Type

Fintech

Logo Text

Bramwell

```html
<!DOCTYPE html>
<html lang="en">
<head>
<meta charset="utf-8">
<title>Bramwell Business Card</title>
<link rel="stylesheet" href="https://fonts.googleapis.com/css2?family=Inter:wght@600&family=Poppins:wght@600&family=Questrial&family=Arimo&display=swap">
<style>
  :root {
    --stage: #000000;
    --navy: #283a5e;
    --card-grey: #bebfc1;
    --band-grey: #a6a7a9;
    --purple-deep: #4d37bd;
    --purple-mid: #6651dc;
    --purple-light: #8a79f1;
    --white: #ffffff;
  }
  * { margin: 0; padding: 0; box-sizing: border-box; }
  html, body { width: 1200px; height: 512px; overflow: hidden; background: var(--stage); }
  .stage { position: relative; width: 1200px; height: 512px; background: var(--stage); }

  .card { position: absolute; top: 139px; width: 411px; height: 235px; overflow: hidden; }
  .card--front { left: 115px; background: var(--card-grey); }
  .card--back { left: 674px; background: var(--navy); }

  .card__bands { position: absolute; inset: 0; width: 100%; height: 100%; }

  .wordmark {
    position: absolute;
    font-family: "Inter", sans-serif;
    font-weight: 600;
    font-size: 38px;
    letter-spacing: -1.5px;
    line-height: 38px;
    height: 38px;
    white-space: nowrap;
  }
  .card--front .wordmark { left: 26px; width: 160px; top: 93px; color: var(--navy); }
  .card--back .wordmark { left: 0; right: 0; text-align: center; top: 99px; color: var(--white); }

  .divider { position: absolute; left: 205px; top: 51px; width: 1.5px; height: 132px; background: var(--navy); }

  .identity { position: absolute; left: 212px; width: 190px; top: 63px; text-align: center; color: var(--navy); }
  .identity__name { font-family: "Poppins", sans-serif; font-weight: 600; font-size: 19px; line-height: 1.05; letter-spacing: 0.3px; }
  .identity__title { font-family: "Questrial", sans-serif; font-size: 16px; line-height: 1.2; letter-spacing: 0.2px; }

  .contact { position: absolute; left: 241px; top: 124px; list-style: none; color: var(--navy);
    font-family: "Arimo", sans-serif; font-size: 12px; line-height: 13.3px; }
  .contact__item { position: relative; padding-left: 13px; }
  .contact__item::before { content: ""; position: absolute; left: 0; top: 4px; width: 6px; height: 6px; background: var(--navy); }
</style>
</head>
<body>
<main class="stage">
  <section class="card card--front" aria-label="Card front">
    <svg class="card__bands" viewBox="0 0 883 504" preserveAspectRatio="none" aria-hidden="true">
      <polygon fill="var(--band-grey)" points="0,0 883,0 883,78 330,78 287,32 0,32"/>
      <rect fill="var(--navy)" x="0" y="0" width="883" height="18"/>
      <polygon fill="var(--purple-light)" points="296,18 418,18 378,64 330,64"/>
      <polygon fill="var(--purple-mid)" points="433,0 530,0 477,64 377,64"/>
      <polygon fill="var(--purple-deep)" points="515,18 583,18 595,0 883,0 883,64 477,64"/>
      <polygon fill="var(--band-grey)" points="0,452 622,452 676,478 883,478 883,504 0,504"/>
      <polygon fill="var(--navy)" points="0,469 655,469 675,494 883,494 883,504 0,504"/>
      <polygon fill="var(--purple-deep)" points="400,469 465,469 437,504 372,504"/>
      <polygon fill="var(--purple-light)" points="465,469 620,469 592,504 437,504"/>
    </svg>
    <div class="wordmark">Bramwell</div>
    <div class="divider"></div>
    <div class="identity">
      <p class="identity__name">JOHN DOE</p>
      <p class="identity__title">GENERAL MANAGER</p>
    </div>
    <ul class="contact">
      <li class="contact__item">National Producer<br>License # 15820374</li>
      <li class="contact__item">service@bramwell.com</li>
      <li class="contact__item">www.bramwell.com</li>
    </ul>
  </section>

  <section class="card card--back" aria-label="Card back">
    <div class="wordmark">Bramwell</div>
  </section>
</main>
</body>
</html>
```